Hopscotch Nell needs updated Marketing Material!

Moving business to a new location and am looking to update all marketing material, including business cards, postcards, flyers, website. I've attached a copy of my current business card.
Updates

Good Morning!  I just received my new business phone number.  It is 583-402-9176

Hello All Designers!

Thank you for all the submissions I have received so far!  I wanted to give you a bit more background on what Hopscotch Nell is all about:

I started this service when I was downsized out of a sales and marketing position.   A friend asked if I had time to run a few errands for her while she was at work.  "Lightbulb"!  I thought there must be more people that are over worked, over booked and want nothing more to do when they get home than spend time with their families or just relaxing.  And who wants to do all their running around on the weekends??  Hopscotch Nell was born!

I have been extremely fortunate with my business here in California.  However, this summer I will be moving to a small town in Pennsylvania and I will be in uncharted territory.  I hope to have marketing material that will "WOW" all new potential clients.  Letting them know that I offer a unique service that can put time back into their week and free up their weekends for more important things.

If there is anything else I can tell you in order to help you with your design process, please let me know!
Thank you!
Nellie

Target Market(s)

Busy working parents and young professionals with disposable income that would like to spend their down time doing things that they enjoy rather than doing errands.

Industry/Entity Type

Marketing

```html
<!DOCTYPE html>
<html lang="en">
<head>
<meta charset="utf-8">
<title>Hopscotch Nell – Business Card</title>
<link rel="stylesheet" href="https://fonts.googleapis.com/css2?family=Cinzel:wght@400;600&family=Tinos&display=swap">
<style>
  :root {
    --backdrop: #e9e7e3;
    --card: #1d1d1e;
    --card-edge: #151516;
    --silver: #d9d9d7;
    --gold: #a8893f;
    --gold-soft: #b79a52;
    --grey-text: #a9a9a6;
    --mark: #0c0c0d;
  }
  * { box-sizing: border-box; margin: 0; padding: 0; }
  html, body {
    width: 1200px;
    height: 801px;
    overflow: hidden;
    background: var(--backdrop);
  }
  .canvas {
    position: relative;
    width: 1200px;
    height: 801px;
    display: flex;
    justify-content: center;
    align-items: center;
    gap: 110px;
  }
  .card {
    position: relative;
    width: 370px;
    height: 620px;
    background: var(--card);
    border: 1px solid var(--card-edge);
    box-shadow: 0 10px 28px rgba(0,0,0,0.18);
  }

  /* Front */
  .brand-mark {
    position: absolute;
    left: 50%;
    top: 170px;
    width: 120px;
    height: 120px;
    margin-left: -60px;
    border-radius: 50%;
    background: var(--mark);
  }
  .brand-name {
    position: absolute;
    left: 0;
    right: 0;
    top: 300px;
    text-align: center;
    font-family: "Cinzel", serif;
    font-weight: 600;
    font-size: 34px;
    line-height: 1.05;
    letter-spacing: 1px;
    color: var(--silver);
  }
  .brand-tagline {
    position: absolute;
    left: 0;
    right: 0;
    bottom: 62px;
    text-align: center;
    font-family: "Tinos", serif;
    font-size: 11px;
    letter-spacing: 0.6px;
    text-transform: uppercase;
    color: var(--grey-text);
  }

  /* Back */
  .owner-name {
    position: absolute;
    left: 0;
    right: 0;
    top: 200px;
    text-align: center;
    font-family: "Cinzel", serif;
    font-size: 25px;
    letter-spacing: 0.5px;
    color: var(--gold);
  }
  .service-list {
    position: absolute;
    left: 0;
    right: 0;
    top: 300px;
    list-style: none;
    text-align: center;
    font-family: "Tinos", serif;
    font-size: 15px;
    line-height: 21px;
    letter-spacing: 0.6px;
    color: var(--gold-soft);
  }
  .service-list .small { font-size: 13px; letter-spacing: 0; }
  .contact-phone {
    position: absolute;
    left: 0;
    right: 0;
    top: 430px;
    text-align: center;
    font-family: "Tinos", serif;
    font-size: 17px;
    letter-spacing: 2px;
    color: var(--grey-text);
  }
  .contact-email {
    position: absolute;
    left: 0;
    right: 0;
    top: 470px;
    text-align: center;
    font-family: "Tinos", serif;
    font-size: 15px;
    letter-spacing: 0.5px;
    color: var(--grey-text);
  }
</style>
</head>
<body>
  <main class="canvas">
    <section class="card card-front" aria-label="Card front">
      <div class="brand-mark" aria-hidden="true"></div>
      <h1 class="brand-name">Hopscotch<br>Nell</h1>
      <p class="brand-tagline">Personal concierge and errand service</p>
    </section>

    <section class="card card-back" aria-label="Card back">
      <h2 class="owner-name">Nellie Harper</h2>
      <ul class="service-list">
        <li>Personal Shopping &amp; Errands</li>
        <li>Household Management</li>
        <li>Corporate Concierge</li>
        <li>Project Management</li>
        <li class="small">Group Rates for Teachers &amp; Seniors</li>
      </ul>
      <p class="contact-phone">+1 &nbsp;583-402-9176</p>
      <p class="contact-email">nellie@hopscotchnell.biz</p>
    </section>
  </main>
</body>
</html>
```